Webpage

I am a professional genealogist. I need a webpage that is professional looking (using the logo I chose), I can add hyperlinks and photos to if and when I want.

```html
<!DOCTYPE html>
<html lang="en">
<head>
<meta charset="utf-8">
<title>Rootline Research Services</title>
<link rel="stylesheet" href="https://fonts.googleapis.com/css2?family=Open+Sans:wght@300;400;600&family=Italianno&display=swap">
<style>
:root{
  --teal:#13a9bf;
  --teal-soft:#7fc9bf;
  --mint:#8fd0b0;
  --sky:#a9cde3;
  --ink:#222;
  --grey-line:#b9b9b9;
  --leaf-dark:#3f7a2a;
  --leaf:#78b04a;
  --leaf-light:#d6ebb8;
  --shirt:#a9d3ec;
  --warm:#e8c9b0;
  --flower-a:#f1f2f8;
  --flower-b:#dfe9cf;
}
*{margin:0;padding:0;box-sizing:border-box}
html,body{width:1200px;height:625px;overflow:hidden;background:#fff}
body{position:relative;font-family:"Open Sans",Arial,sans-serif;color:var(--ink)}
.top-band{position:absolute;left:0;top:0;width:1200px;height:40px;border-top:4px solid var(--teal);background:linear-gradient(#d9f1f8,#fff)}
.utility{position:absolute;top:8px;left:946px;display:flex;gap:16px}
.brand{position:absolute;left:222px;top:26px;display:flex;align-items:center;gap:14px}
.brand-mark{width:54px;height:54px;border-radius:50%;background:var(--teal-soft)}
.brand-name{font-size:16px;font-weight:400;color:var(--ink);line-height:18px;white-space:nowrap;text-align:right}
.brand-name span{display:block}
.main-nav{position:absolute;right:210px;top:42px;display:flex;gap:11px;font-size:12px}
.main-nav a{color:var(--ink);text-decoration:none}
.hero-shadow{position:absolute;top:225px;width:60px;height:110px}
.hero-shadow.left{left:180px;transform:skewY(-10deg);background:linear-gradient(90deg,rgba(0,0,0,0),rgba(0,0,0,.3))}
.hero-shadow.right{left:985px;transform:skewY(10deg);background:linear-gradient(90deg,rgba(0,0,0,.3),rgba(0,0,0,0))}
.hero{position:absolute;left:216px;top:95px;width:774px;height:257px;
  background:
    linear-gradient(180deg,rgba(255,255,255,0) 55%,rgba(169,211,236,.85) 85%,var(--shirt)),
    radial-gradient(ellipse 40% 45% at 50% 55%,var(--warm),rgba(232,201,176,0) 70%),
    linear-gradient(100deg,var(--leaf-dark),var(--leaf) 30%,var(--leaf-light) 60%,var(--leaf) 85%,var(--leaf-dark))}
.hero-caption{position:absolute;left:216px;top:316px;width:311px;height:36px;background:rgba(255,255,255,.85);font-weight:300;font-size:24px;letter-spacing:-.4px;padding-left:10px;line-height:36px;color:#333;white-space:nowrap;overflow:hidden}
.rule{position:absolute;left:216px;top:356px;width:772px;height:4px;border-top:1px solid var(--grey-line);border-bottom:1px solid var(--grey-line)}
.portrait{position:absolute;left:860px;top:309px;width:97px;height:98px;border:5px solid #fff;box-shadow:0 1px 5px rgba(0,0,0,.45);background:radial-gradient(ellipse 45% 50% at 50% 45%,#d9c4b4,#b0b0b0 70%),#aaa}
.title{position:absolute;left:218px;top:362px;white-space:nowrap;font-weight:400}
.title-name{font-family:"Italianno",cursive;font-size:60px;color:var(--teal)}
.title-role{font-family:"Italianno",cursive;font-size:30px;color:var(--ink)}
.contact{position:absolute;left:218px;top:440px;display:flex;font-size:13px;line-height:20px;font-style:normal}
.contact-col{width:139px}
.contact-col+.contact-col{width:auto;border-left:1px solid var(--grey-line);padding-left:18px;height:56px}
.flowers{position:absolute;left:860px;top:410px;width:340px;height:215px;background:radial-gradient(circle at 75% 75%,var(--flower-b),var(--flower-a) 55%,#fff)}
.waves{position:absolute;left:0;top:560px}
.copyright{position:absolute;left:528px;top:609px;font-size:8px;color:#333}
</style>
</head>
<body>
<div class="top-band"></div>
<nav class="utility" aria-label="Quick links">
  <svg width="13" height="12" viewBox="0 0 13 12"><path d="M6.5 0 13 6H11v6H8V8H5v4H2V6H0z" fill="#111"/></svg>
  <svg width="13" height="10" viewBox="0 0 13 10"><rect width="13" height="10" fill="#111"/><path d="M0 0l6.5 5L13 0" stroke="#fff" fill="none"/></svg>
</nav>
<header class="brand">
  <span class="brand-mark"></span>
  <span class="brand-name"><span>Rootline Research</span><span>Services</span></span>
</header>
<nav class="main-nav">
  <a href="#">About</a><a href="#">Services</a><a href="#">Publications</a><a href="#">Blog</a>
</nav>
<div class="hero-shadow left"></div>
<div class="hero-shadow right"></div>
<div class="hero" role="img" aria-label="Photo of a smiling three-generation family outdoors among green trees"></div>
<div class="hero-caption">Rootline Research Services</div>
<div class="rule"></div>
<div class="portrait" role="img" aria-label="Portrait photo of the genealogist"></div>
<h1 class="title"><span class="title-name">Dana Ashford</span> <span class="title-role">- Professional Genealogist</span></h1>
<address class="contact">
  <div class="contact-col">PO Box 48213<br>Cedar Falls, TX 75001</div>
  <div class="contact-col">Phone: 555-014-2270<br>Email: dana@example.net</div>
</address>
<div class="flowers" role="img" aria-label="Photo of white lilies and roses"></div>
<svg class="waves" width="860" height="65" viewBox="0 0 860 65">
  <path d="M0 16 C150 4 330 10 425 28 L0 46Z" fill="var(--teal)"/>
  <path d="M0 38 Q250 28 450 65 L0 65Z" fill="var(--sky)"/>
  <path d="M0 38 Q250 28 450 65" stroke="#fff" stroke-width="2" fill="none"/>
  <path d="M290 65 Q560 15 860 65Z" fill="var(--mint)"/>
</svg>
<p class="copyright">Copyright © 2014. All Rights Reserved.</p>
</body>
</html>
```